New Business Card/Website Logo

We need a business card design for a new company based in Sydney. The company focuses mainly in construction in the field of form work and concreting. Attached is the logo being used already which can be used as a base for a new design, the current one is simply too bland and we are looking to spruce it up so it stands out and looks nicer. The logo would also be used on the website which is currently under construction. The attached image has the name, mobile and also the license number which needs to be there. The current email address on there can be removed and can be replaced with the website http://www.bravelintel.com.au, thanks!
Updates

Target Market(s)

Construction industry. Focusing on form work and concreting

Industry/Entity Type

Construction

Requirements
Must have
• License # on card along with website http://www.bravelintel.com.au and mobile phone number
Nice to have
• You have freedom with the design. The current design was a mock up done quite quickly. Please just keep in mind the target audience - construction, thanks.
Should not have
• the mailvista email address can be removed(refer picture) and replaced somewhere on the design with the website http://www.bravelintel.com.au

```html
<!DOCTYPE html>
<html lang="en">
<head>
<meta charset="UTF-8">
<title>Bravelintel Business Card</title>
<link href="https://fonts.googleapis.com/css2?family=Arimo:wght@400;700&display=swap" rel="stylesheet">
<style>
  :root {
    --backdrop: #1b1b1b;
    --card: #2b2b2b;
    --card-deep: #232323;
    --tile: rgba(255, 255, 255, 0.04);
    --tile-dark: rgba(0, 0, 0, 0.18);
    --green: #3dbd45;
    --white: #f4f4f4;
    --grey: #c9c9c9;
  }
  * { margin: 0; padding: 0; box-sizing: border-box; }
  html, body {
    width: 1200px;
    height: 900px;
    overflow: hidden;
    background: var(--backdrop);
    font-family: "Arimo", Arial, sans-serif;
  }
  .stage {
    width: 1200px;
    height: 900px;
    display: flex;
    align-items: center;
    justify-content: center;
  }
  .card {
    position: relative;
    width: 460px;
    height: 760px;
    background: linear-gradient(160deg, var(--card) 0%, var(--card-deep) 100%);
    overflow: hidden;
    box-shadow: 0 20px 50px rgba(0, 0, 0, 0.6);
  }
  .card-tiles {
    position: absolute;
    inset: 0;
  }
  .brand {
    position: absolute;
    left: 40px;
    top: 120px;
    display: flex;
    align-items: center;
    gap: 14px;
  }
  .brand-square {
    width: 30px;
    height: 30px;
    background: var(--green);
  }
  .brand-name {
    font-weight: 700;
    font-size: 40px;
    letter-spacing: 2px;
    color: var(--green);
  }
  .contact {
    position: absolute;
    left: 30px;
    right: 30px;
    top: 260px;
  }
  .person-name {
    display: inline-block;
    margin-left: 80px;
    background: var(--green);
    color: var(--white);
    font-weight: 700;
    font-size: 30px;
    padding: 3px 10px;
    border-radius: 3px;
  }
  .phone {
    margin-top: 58px;
    font-weight: 700;
    font-size: 32px;
    color: var(--white);
    letter-spacing: 1px;
  }
  .website {
    margin-top: 80px;
    display: inline-block;
    line-height: 1;
  }
  .website-prefix {
    display: block;
    font-weight: 700;
    font-size: 22px;
    color: var(--green);
  }
  .website-name {
    display: block;
    font-weight: 700;
    font-size: 48px;
    color: var(--white);
  }
  .website-suffix {
    display: block;
    text-align: right;
    font-size: 22px;
    color: var(--green);
  }
  .licence {
    position: absolute;
    left: 30px;
    bottom: 44px;
    font-size: 17px;
    color: var(--grey);
  }
</style>
</head>
<body>
  <main class="stage">
    <article class="card">
      <svg class="card-tiles" width="460" height="760" viewBox="0 0 460 760" aria-hidden="true">
        <rect x="250" y="30" width="150" height="190" fill="var(--tile)"/>
        <rect x="300" y="200" width="120" height="330" fill="var(--tile-dark)"/>
        <rect x="180" y="260" width="90" height="260" fill="var(--tile)"/>
        <rect x="380" y="330" width="80" height="260" fill="var(--tile)"/>
        <rect x="260" y="520" width="160" height="150" fill="var(--tile-dark)"/>
        <rect x="120" y="420" width="70" height="180" fill="var(--tile-dark)"/>
      </svg>

      <div class="brand">
        <span class="brand-square"></span>
        <span class="brand-name">BRAVELINTEL</span>
      </div>

      <section class="contact">
        <span class="person-name">Marco Deluca</span>
        <p class="phone">0412 508 374</p>
        <div class="website">
          <span class="website-prefix">www.</span>
          <span class="website-name">bravelintel</span>
          <span class="website-suffix">.com.au</span>
        </div>
      </section>

      <p class="licence">Licence : 384215B</p>
    </article>
  </main>
</body>
</html>
```